Aviation Banner Ad Designs

SkyLedgerMetrics provides access to the most accurate aircraft operating cost information, to compare Piston, Turboprop and Jet aircraft.

The banners ads will be used for retargeting/remarketing - to bring visitors back to the site. The banners should remind and reinforce the key messages of what the site provides.

Target Market(s)

Private aircraft buyers including:
- Aircraft Brokers
- Charter Operators
- Corporate Flight Departments
- Aircraft Management companies
- Financial Institutions
- Aircraft Owners
- Prospective Buyers

Requirements
Must have
• A. Banner Objective
The visual and textual content of the banner should remind the viewer about the features of the site, and prompt them to return to the site.
1. Arresting visual
2. Headline
3. Single message
4. Compelling CTA
5. Logo - big enough to see
6. Standard DWR ad sizes/specs

B. Design Elements
Logo: As attached
Main Title: Calculate Jet Operating Costs
Subtitle: Compare Ownership Usage Scenarios
Call to Action Button: Compare Ownership Costs
Background: Several images supplied as options

C. Banner Sizes
Do examples as 300×250 , 728×90 , 160×600
Final sizes to also include 320×100 , 336x280 , 300x600

Finally delivery as .jpg files.

Font - use same font as on site

```html
<!DOCTYPE html>
<html lang="en">
<head>
<meta charset="utf-8">
<title>SkyLedgerMetrics – Banner Set</title>
<link rel="stylesheet" href="https://fonts.googleapis.com/css2?family=Oswald:wght@500;700&family=Noto+Sans:wght@500&display=swap">
<style>
  :root {
    --page: #d9d9d9;
    --white: #ffffff;
    --red: #d71f26;
    --red-dark: #8e0f12;
    --red-deep: #6e0a0c;
    --navy: #2b3990;
    --ink: #1b1b1b;
    --rule: #b9b9b9;
    --bar: #f1f1f1;
    --sky: #8fb0d6;
    --sky-deep: #4f74b3;
    --metal: #d9cfae;
  }
  * { box-sizing: border-box; margin: 0; padding: 0; }
  html, body { width: 1200px; height: 2400px; overflow: hidden; }
  body { background: var(--page); position: relative; font-family: "Noto Sans", Arial, sans-serif; }

  .banner { position: absolute; overflow: hidden; background: var(--white); box-shadow: 0 10px 18px rgba(0,0,0,.28); }
  .banner > * { position: absolute; }

  .brand { display: flex; align-items: center; gap: 10px; font-family: "Noto Sans", Arial, sans-serif; font-weight: 500; color: var(--ink); letter-spacing: .5px; }
  .brand-mark { background: var(--red); flex: none; }

  .headline { font-family: "Oswald", "Arial Narrow", sans-serif; font-weight: 700; color: var(--red); text-transform: uppercase; line-height: 1.03; letter-spacing: .3px; }
  .subtitle { font-family: "Noto Sans", Arial, sans-serif; font-weight: 500; color: var(--navy); line-height: 1.25; }

  .cta {
    display: flex; align-items: center; justify-content: center;
    border-radius: 999px; color: var(--white);
    font-family: "Oswald", "Arial Narrow", sans-serif; font-weight: 500; text-transform: uppercase; letter-spacing: .3px;
    background: linear-gradient(180deg, var(--red) 0%, #b8161b 55%, var(--red-dark) 100%);
    box-shadow: 0 5px 8px rgba(0,0,0,.25);
  }

  .device-art { background: linear-gradient(180deg, #f4f4f4, #dcdcdc); border-radius: 4px; }

  /* 300×250 */
  .banner-square { left: 100px; top: 59px; width: 1000px; height: 833px; }
  .banner-square .shapes { left: 0; top: 0; width: 1000px; height: 833px; }
  .banner-square .brand { left: 30px; top: 52px; font-size: 30px; }
  .banner-square .brand-mark { width: 26px; height: 26px; }
  .banner-square .headline { left: 20px; top: 160px; font-size: 72px; }
  .banner-square .rule { left: 18px; top: 326px; width: 464px; height: 3px; background: var(--rule); }
  .banner-square .subtitle { left: 30px; top: 362px; width: 400px; font-size: 35px; text-align: center; }
  .banner-square .device-art { left: 42px; top: 478px; width: 362px; height: 170px; }
  .banner-square .cta { left: 22px; top: 663px; width: 388px; height: 77px; font-size: 30px; }

  /* 728×90 */
  .banner-leader { left: 31px; top: 958px; width: 1111px; height: 347px; }
  .banner-leader .shapes { left: 0; top: 0; width: 1111px; height: 347px; }
  .banner-leader .brand { left: 24px; top: 34px; font-size: 24px; }
  .banner-leader .brand-mark { width: 20px; height: 20px; }
  .banner-leader .headline { left: 20px; top: 104px; font-size: 60px; }
  .banner-leader .subtitle { left: 22px; top: 253px; font-size: 23px; }
  .banner-leader .cta { left: 266px; top: 252px; width: 305px; height: 60px; font-size: 22px; }

  /* 160×600 */
  .banner-sky { left: 352px; top: 1386px; width: 469px; height: 939px; background: linear-gradient(180deg, var(--red) 40%, var(--red-deep) 100%); }
  .banner-sky .shapes { left: 0; top: 0; width: 469px; height: 939px; }
  .banner-sky .brand { left: 265px; top: 30px; font-size: 16px; gap: 7px; }
  .banner-sky .brand-mark { width: 14px; height: 14px; }
  .banner-sky .headline { left: 27px; top: 502px; font-size: 50px; color: var(--white); }
  .banner-sky .sub-card { left: 26px; top: 686px; width: 417px; height: 81px; background: var(--white); box-shadow: 0 8px 10px rgba(0,0,0,.25); }
  .banner-sky .sub-card .subtitle { position: absolute; left: 17px; top: 15px; font-size: 19px; color: var(--red); }
  .banner-sky .sub-card .device-art { position: absolute; left: 240px; top: 8px; width: 170px; height: 66px; }
  .banner-sky .cta { left: 84px; top: 842px; width: 300px; height: 58px; font-size: 21px; }
</style>
</head>
<body>

<section class="banner banner-square" aria-label="300 by 250 banner">
  <svg class="shapes" viewBox="0 0 1000 833" aria-hidden="true">
    <path d="M842 0 L1000 0 L1000 833 L366 833 L612 620 Q650 585 612 560 L440 455 Q405 432 432 400 Z" fill="#c4c4c4"/>
    <path d="M852 0 L1000 0 L1000 833 L385 833 L630 620 Q668 585 630 560 L458 455 Q423 432 450 400 Z" fill="var(--red)"/>
  </svg>
  <svg class="shapes" viewBox="0 0 1000 833" role="img" aria-label="Photo: close-up of a private jet engine and airstair on the ramp">
    <defs>
      <linearGradient id="sq-photo" x1="0" y1="0" x2="0" y2="1">
        <stop offset="0" stop-color="var(--sky)"/>
        <stop offset=".6" stop-color="#b9c6d4"/>
        <stop offset="1" stop-color="var(--metal)"/>
      </linearGradient>
    </defs>
    <path d="M895 0 L1000 0 L1000 833 L440 833 L672 622 Q708 585 672 556 L495 455 Q470 436 492 410 Z" fill="url(#sq-photo)"/>
  </svg>
  <div class="brand"><span class="brand-mark"></span>SkyLedgerMetrics</div>
  <h1 class="headline">Calculate Jet<br>Operating Costs</h1>
  <div class="rule"></div>
  <p class="subtitle">Compare Ownership<br>Usage Scenarios</p>
  <div class="device-art" role="img" aria-label="Illustration: desktop, laptop, tablet and phone showing aircraft cost charts"></div>
  <a class="cta">Compare Ownership Costs</a>
</section>

<section class="banner banner-leader" aria-label="728 by 90 banner">
  <svg class="shapes" viewBox="0 0 1111 347" aria-hidden="true">
    <rect x="355" y="104" width="36" height="243" fill="var(--bar)"/>
    <rect x="413" y="10" width="36" height="337" fill="var(--bar)"/>
    <rect x="472" y="185" width="36" height="162" fill="var(--bar)"/>
    <rect x="532" y="167" width="36" height="180" fill="var(--bar)"/>
    <path d="M740 0 L757 0 L582 347 L565 347 Z" fill="var(--red)"/>
  </svg>
  <svg class="shapes" viewBox="0 0 1111 347" role="img" aria-label="Photo: white private jets with tail engines against a blue sky">
    <defs>
      <linearGradient id="ld-photo" x1="0" y1="0" x2="0" y2="1">
        <stop offset="0" stop-color="var(--sky-deep)"/>
        <stop offset=".7" stop-color="#a9c0de"/>
        <stop offset="1" stop-color="#dfe6ef"/>
      </linearGradient>
    </defs>
    <path d="M762 0 L1111 0 L1111 347 L588 347 Z" fill="url(#ld-photo)"/>
  </svg>
  <div class="brand"><span class="brand-mark"></span>SkyLedgerMetrics</div>
  <h1 class="headline">Calculate Jet<br>Operating Costs</h1>
  <p class="subtitle">Compare Ownership<br>Usage Scenarios</p>
  <a class="cta">Compare Ownership Costs</a>
</section>

<section class="banner banner-sky" aria-label="160 by 600 banner">
  <svg class="shapes" viewBox="0 0 469 939" aria-hidden="true">
    <path d="M20 0 L469 0 L469 374 Q380 345 300 380 Q190 432 110 430 Q60 425 48 360 Q30 250 20 150 Z" fill="#dedede"/>
    <rect x="305" y="454" width="24" height="155" fill="#c8151b" opacity=".8"/>
    <rect x="345" y="390" width="24" height="219" fill="#c8151b" opacity=".8"/>
    <rect x="385" y="505" width="24" height="104" fill="#c8151b" opacity=".8"/>
    <rect x="425" y="495" width="24" height="114" fill="#c8151b" opacity=".8"/>
  </svg>
  <svg class="shapes" viewBox="0 0 469 939" role="img" aria-label="Photo: business jet climbing through a sunset sky">
    <defs>
      <linearGradient id="sk-photo" x1="0" y1="0" x2="0" y2="1">
        <stop offset="0" stop-color="#a9b4c0"/>
        <stop offset=".55" stop-color="#e3d2bd"/>
        <stop offset="1" stop-color="#e9b786"/>
      </linearGradient>
    </defs>
    <path d="M28 0 L469 0 L469 365 Q380 335 300 370 Q190 420 112 420 Q66 415 56 355 Q38 250 28 150 Z" fill="url(#sk-photo)"/>
  </svg>
  <div class="brand"><span class="brand-mark"></span>SkyLedgerMetrics</div>
  <h1 class="headline">Calculate Jet<br>Operating Costs</h1>
  <div class="sub-card">
    <p class="subtitle">Compare Ownership<br>Usage Scenarios</p>
    <div class="device-art" role="img" aria-label="Illustration: desktop, laptop, tablet and phone showing aircraft cost charts"></div>
  </div>
  <a class="cta">Compare Ownership Costs</a>
</section>

</body>
</html>
```